" Consultora em investimentos nos EUA através de aplicações financeiras com resgate do capital após determinado período de tempo. Está incluído no projeto de investimento um seguro de vida internacional que proporciona segurança para si próprio e para sua família. Ou seja nosso cliente investe em dólares em determinado tempo onde durante o período esta coberto por um seguro de vida. No final do período não utilizando o seguro tudo aquilo que investiu retorna ao cliente capitalizado. "

```html
<!DOCTYPE html>
<html lang="pt-BR">
<head>
<meta charset="utf-8">
<title>Brightmoor – Cartão de visita</title>
<link rel="stylesheet" href="https://fonts.googleapis.com/css2?family=Montserrat:wght@300;400;500;600&family=Open+Sans:wght@400;600&display=swap">
<style>
  :root {
    --bg: #e4e5e7;
    --navy: #22242f;
    --navy-deep: #1b1d26;
    --gold: #c9a85a;
    --gold-light: #e6cf8e;
    --white: #ffffff;
    --ink: #2a2c35;
    --muted: #6b6d75;
  }
  * { box-sizing: border-box; margin: 0; padding: 0; }
  html, body { width: 1200px; height: 1200px; overflow: hidden; }
  body {
    background: var(--bg);
    display: flex;
    flex-direction: column;
    align-items: center;
    justify-content: center;
    gap: 64px;
    font-family: "Open Sans", sans-serif;
  }
  .card {
    position: relative;
    width: 900px;
    height: 500px;
    overflow: hidden;
    box-shadow: 0 14px 30px rgba(0,0,0,0.18);
  }
  .gold-edge {
    position: absolute;
    left: 0; right: 0; bottom: 0;
    height: 14px;
    background: linear-gradient(90deg, var(--gold), var(--gold-light), var(--gold));
  }
  .gold-side {
    position: absolute;
    top: 0; bottom: 0; right: 0;
    width: 14px;
    background: linear-gradient(180deg, var(--gold-light), var(--gold));
  }

  /* Front */
  .card-front {
    background: linear-gradient(135deg, var(--navy) 0%, var(--navy-deep) 100%);
    display: flex;
    align-items: center;
    justify-content: center;
  }
  .brand {
    display: flex;
    flex-direction: column;
    align-items: center;
    gap: 22px;
  }
  .brand-square {
    width: 70px; height: 70px;
    background: var(--gold);
  }
  .brand-name {
    font-family: "Montserrat", sans-serif;
    font-weight: 400;
    font-size: 58px;
    letter-spacing: 10px;
    color: var(--white);
  }
  .brand-tagline {
    font-family: "Montserrat", sans-serif;
    font-weight: 500;
    font-size: 13px;
    letter-spacing: 5px;
    color: var(--gold);
    margin-top: -14px;
  }

  /* Back */
  .card-back {
    background: var(--white);
    display: grid;
    grid-template-columns: 1fr 1fr;
  }
  .back-brand {
    display: flex;
    align-items: center;
    justify-content: center;
  }
  .back-brand .brand-square { width: 56px; height: 56px; }
  .back-brand .brand-name { color: var(--ink); font-size: 40px; letter-spacing: 7px; }
  .back-brand .brand-tagline { font-size: 10px; letter-spacing: 4px; margin-top: -12px; }
  .contact {
    border-left: 2px solid var(--gold);
    margin: 60px 0 70px;
    padding: 10px 0 0 44px;
    color: var(--ink);
  }
  .contact-name {
    font-family: "Montserrat", sans-serif;
    font-size: 30px;
    font-weight: 500;
  }
  .contact-role {
    font-size: 15px;
    color: var(--muted);
    margin: 4px 0 28px;
  }
  .contact-list { list-style: none; display: flex; flex-direction: column; gap: 14px; }
  .contact-list li {
    display: flex; align-items: center; gap: 14px;
    font-size: 16px;
  }
  .contact-list svg { width: 18px; height: 18px; flex: none; }
</style>
</head>
<body>

  <section class="card card-front">
    <div class="brand">
      <div class="brand-square"></div>
      <div class="brand-name">BRIGHTMOOR</div>
      <div class="brand-tagline">CONSULTORIA EM INVESTIMENTOS</div>
    </div>
    <div class="gold-edge"></div>
  </section>

  <section class="card card-back">
    <div class="back-brand">
      <div class="brand">
        <div class="brand-square"></div>
        <div class="brand-name">BRIGHTMOOR</div>
        <div class="brand-tagline">CONSULTORIA EM INVESTIMENTOS</div>
      </div>
    </div>
    <div class="contact">
      <div class="contact-name">Nome Sobrenome</div>
      <div class="contact-role">Cargo</div>
      <ul class="contact-list">
        <li>
          <svg viewBox="0 0 24 24"><path fill="#c9a85a" d="M6.6 10.8a15 15 0 0 0 6.6 6.6l2.2-2.2a1 1 0 0 1 1-.25 11.4 11.4 0 0 0 3.6.57 1 1 0 0 1 1 1V20a1 1 0 0 1-1 1A17 17 0 0 1 3 4a1 1 0 0 1 1-1h3.5a1 1 0 0 1 1 1c0 1.25.2 2.45.57 3.57a1 1 0 0 1-.25 1z"/></svg>
          +55 11 9 9999 9999
        </li>
        <li>
          <svg viewBox="0 0 24 24"><path fill="#c9a85a" d="M6.6 10.8a15 15 0 0 0 6.6 6.6l2.2-2.2a1 1 0 0 1 1-.25 11.4 11.4 0 0 0 3.6.57 1 1 0 0 1 1 1V20a1 1 0 0 1-1 1A17 17 0 0 1 3 4a1 1 0 0 1 1-1h3.5a1 1 0 0 1 1 1c0 1.25.2 2.45.57 3.57a1 1 0 0 1-.25 1z"/></svg>
          +55 11 9 9999 9999
        </li>
        <li>
          <svg viewBox="0 0 24 24"><rect x="2" y="5" width="20" height="14" rx="1.5" fill="#c9a85a"/><path d="M3 6l9 7 9-7" stroke="#fff" stroke-width="1.6" fill="none"/></svg>
          exemplo@brightmoor.com.br
        </li>
        <li>
          <svg viewBox="0 0 24 24"><circle cx="12" cy="12" r="9" fill="none" stroke="#c9a85a" stroke-width="2"/><path d="M3 12h18M12 3c3 3.5 3 14.5 0 18M12 3c-3 3.5-3 14.5 0 18" stroke="#c9a85a" stroke-width="1.6" fill="none"/></svg>
          www.site.com.br
        </li>
        <li>
          <svg viewBox="0 0 24 24"><path fill="#c9a85a" d="M12 2a7 7 0 0 0-7 7c0 5.2 7 13 7 13s7-7.8 7-13a7 7 0 0 0-7-7zm0 9.5A2.5 2.5 0 1 1 12 6.5a2.5 2.5 0 0 1 0 5z"/></svg>
          Endereço: Exemplo - Exemplo
        </li>
      </ul>
    </div>
    <div class="gold-side"></div>
  </section>

</body>
</html>
```